Update to Software Toolbar Buttons Design

I am preparing to issue a new version of my product utility software and am looking to freshen up the look of the primary toolbar buttons. Over time the design continuity has drifted a bit and I want to take this opportunity to reassert a common graphic theme. I am primarily interested in freshening up the look and feel, currently represented in the New Toolbar image provided. Though I am not especially looking for a wholesale change in the look and feel, am open to compelling suggestions that deviate from the current presentation. My KPL software provides utilities for use with my primary hardware product. KPL software is used by a variety of people such as engineering professionals, research scientists, graphics artists, high school students, and makers. More information can be gleaned by reviewing my web site www.dolqitek.net, or doing general searches on the trademark Haldentrax. I have provided the associated help file so that you can better understand the function of each button. I have also provided the source Adobe Illustrator file used in generating icons for the current new toolbar design. I want finished work to be provided back in this same format.

```html
<!DOCTYPE html>
<html lang="en">
<head>
<meta charset="utf-8">
<title>Haldentrax Utility Software – Toolbar</title>
<link href="https://fonts.googleapis.com/css2?family=Ubuntu:wght@400;500&display=swap" rel="stylesheet">
<style>
  :root{
    --page:#ffffff;
    --frame:#6b6b6b;
    --panel:#f0f0f0;
    --titlebar:#fbfbfb;
    --panel-edge:#b4b4b8;
    --shadow:#a9a9ad;
    --ink:#111111;
    --coord:#1e73d2;
    --icon-blue:#1a9ad6;
    --icon-light:#8fd3f0;
    --red:#e8141a;
    --grey:#8a8a8a;
    --green:#6cc43a;
    --green-dark:#4fa524;
    --sep:#cfe3cf;
    --field:#f6f6f6;
    --field-text:#a0a0a0;
  }
  *{box-sizing:border-box;margin:0;padding:0}
  html,body{width:1200px;height:1079px;overflow:hidden;background:var(--page)}
  body{font-family:"Ubuntu",sans-serif;color:var(--ink)}
  .canvas{position:relative;width:1200px;height:1079px;border:1px solid var(--frame);background:var(--page)}
  .window{position:absolute;left:72px;width:1057px;height:242px;background:var(--panel);
    border:1px solid var(--panel-edge);border-radius:14px;box-shadow:4px 4px 0 var(--shadow);overflow:hidden}
  .w1{top:142px}.w2{top:420px}.w3{top:709px}
  .titlebar{position:absolute;left:0;top:0;width:100%;height:43px;background:var(--titlebar)}
  .app-mark{position:absolute;left:17px;top:11px;width:22px;height:22px;background:var(--coord);border-radius:3px}
  .app-title{position:absolute;left:55px;top:12px;font-size:17px;line-height:20px;white-space:nowrap}
  .sep{position:absolute;top:60px;width:1px;height:46px;background:var(--sep)}
  .tool{position:absolute;top:57px;width:46px;height:46px;border-radius:8px}
  .tool.active{background:#fff;box-shadow:0 0 0 1px #e4e4e4}
  .tool svg{width:46px;height:46px;display:block}
  .status{position:absolute;left:623px;top:70px;font-size:17px;line-height:20px}
  .connect{position:absolute;left:977px;top:49px;width:50px;height:50px;border-radius:50%;
    background:radial-gradient(circle at 40% 35%,#8fdc5c,var(--green) 55%,var(--green-dark));
    box-shadow:2px 3px 4px rgba(0,0,0,.25)}
  .connect svg{width:50px;height:50px}
  .coord{position:absolute;top:116px;font-size:64px;line-height:64px;color:var(--coord);letter-spacing:1px;white-space:nowrap}
  .cx{left:18px}.cy{left:377px}.cz{left:727px}
  .check{position:absolute;top:194px;width:18px;height:18px;background:#fff;border:1px solid #cfcfcf}
  .label{position:absolute;top:194px;font-size:16px;line-height:20px;white-space:nowrap}
  .field{position:absolute;top:188px;width:254px;height:28px;background:var(--field);
    border-top:1px solid #cdcdcd;border-left:1px solid #cdcdcd;font-size:16px;line-height:20px;color:var(--field-text);padding:4px 5px}
</style>
</head>
<body>
<svg width="0" height="0" style="position:absolute" aria-hidden="true">
  <defs>
    <symbol id="i-xyz" viewBox="0 0 46 46">
      <g fill="none" stroke="var(--icon-light)" stroke-dasharray="2 1.5"><rect x="14" y="6" width="8" height="7"/><rect x="24" y="6" width="8" height="7"/><rect x="34" y="6" width="8" height="7"/><rect x="14" y="32" width="8" height="7"/><rect x="24" y="32" width="8" height="7"/><rect x="34" y="32" width="8" height="7"/></g>
      <path d="M4 24l4 5 7-10" fill="none" stroke="#8cc63f" stroke-width="2.5"/>
      <text x="15" y="30" font-family="Ubuntu,sans-serif" font-size="14" fill="var(--icon-blue)">XYZ</text>
    </symbol>
    <symbol id="i-grid" viewBox="0 0 46 46">
      <g fill="none" stroke="var(--icon-light)" stroke-width="1.5"><rect x="5" y="7" width="10" height="9"/><rect x="17" y="7" width="10" height="9"/><rect x="5" y="18" width="10" height="9"/><rect x="29" y="18" width="10" height="9"/><rect x="17" y="29" width="10" height="9"/><rect x="29" y="29" width="10" height="9"/></g>
      <g fill="none" stroke="var(--icon-blue)" stroke-width="1.5"><rect x="29" y="7" width="10" height="9"/><rect x="5" y="29" width="10" height="9"/></g>
      <path d="M16 27L33 10" stroke="var(--grey)" stroke-width="5" stroke-linecap="round"/>
      <circle cx="15" cy="28" r="5" fill="var(--red)"/>
    </symbol>
    <symbol id="i-axes" viewBox="0 0 46 46">
      <g stroke="var(--icon-blue)" stroke-width="2" fill="var(--icon-blue)">
        <path d="M10 34V12"/><path d="M5 14l5-8 5 8z"/>
        <path d="M10 34H34"/><path d="M32 29l8 5-8 5z"/>
        <path d="M10 34L36 12"/><path d="M30 11l9-2-4 8z"/>
      </g>
      <g font-family="Ubuntu,sans-serif" font-size="7" fill="var(--icon-blue)"><text x="16" y="7">Z</text><text x="41" y="12">Y</text><text x="41" y="40">X</text></g>
      <circle cx="10" cy="34" r="5" fill="var(--red)"/>
    </symbol>
    <symbol id="i-timer" viewBox="0 0 46 46">
      <circle cx="14" cy="16" r="9" fill="none" stroke="var(--icon-blue)" stroke-width="1.5"/>
      <path d="M14 10v6l4 3" fill="none" stroke="var(--icon-blue)" stroke-width="1.5"/>
      <path d="M6 34q10 10 24 3" fill="none" stroke="#555" stroke-dasharray="1 2"/>
      <path d="M36 6v22" stroke="var(--grey)" stroke-width="5" stroke-linecap="round"/>
      <circle cx="36" cy="34" r="6" fill="var(--red)"/>
    </symbol>
    <symbol id="i-layers" viewBox="0 0 46 46">
      <path d="M5 10l10 3v18l-10-3z" fill="#3fb6ea"/>
      <path d="M15 13l12-3v18l-12 3z" fill="#2aa6e0"/>
      <path d="M20 16l10-3 10 3v20l-10 3-10-3z" fill="var(--icon-blue)"/>
    </symbol>
    <symbol id="i-gear" viewBox="0 0 46 46">
      <g fill="var(--icon-blue)">
        <circle cx="23" cy="23" r="11"/>
        <g><rect x="20" y="6" width="6" height="34" rx="1"/><rect x="20" y="6" width="6" height="34" rx="1" transform="rotate(45 23 23)"/><rect x="20" y="6" width="6" height="34" rx="1" transform="rotate(90 23 23)"/><rect x="20" y="6" width="6" height="34" rx="1" transform="rotate(135 23 23)"/></g>
      </g>
      <circle cx="23" cy="23" r="5" fill="var(--panel)"/>
    </symbol>
    <symbol id="i-probe" viewBox="0 0 46 46">
      <path d="M18 28L40 8" stroke="var(--grey)" stroke-width="7" stroke-linecap="round"/>
      <circle cx="15" cy="32" r="10" fill="var(--red)"/>
    </symbol>
    <symbol id="i-info" viewBox="0 0 46 46">
      <circle cx="23" cy="23" r="19" fill="#f7f7f7"/>
      <circle cx="22" cy="10" r="3.2" fill="var(--coord)"/>
      <rect x="19" y="16" width="6" height="18" fill="var(--coord)"/>
    </symbol>
    <symbol id="i-help" viewBox="0 0 46 46">
      <circle cx="23" cy="23" r="19" fill="#f7f7f7"/>
      <text x="23" y="35" text-anchor="middle" font-family="Ubuntu,sans-serif" font-size="34" fill="var(--coord)">?</text>
    </symbol>
    <symbol id="i-connect" viewBox="0 0 50 50">
      <rect x="16" y="12" width="18" height="26" rx="3" fill="none" stroke="#fff" stroke-width="4"/>
      <rect x="12" y="23" width="26" height="4" fill="#fff"/>
      <rect x="22" y="23" width="6" height="4" fill="var(--green)"/>
    </symbol>
  </defs>
</svg>

<main class="canvas">
  <section class="window w1">
    <header class="titlebar"><span class="app-mark"></span><span class="app-title">Haldentrax Utility Software - 7.3</span></header>
    <span class="sep" style="left:15px"></span><span class="sep" style="left:71px"></span><span class="sep" style="left:134px"></span><span class="sep" style="left:197px"></span><span class="sep" style="left:260px"></span><span class="sep" style="left:322px"></span><span class="sep" style="left:385px"></span><span class="sep" style="left:448px"></span><span class="sep" style="left:512px"></span><span class="sep" style="left:573px"></span>
    <div class="tool active" style="left:20px"><svg><use href="#i-xyz"/></svg></div>
    <div class="tool" style="left:80px"><svg><use href="#i-grid"/></svg></div>
    <div class="tool" style="left:142px"><svg><use href="#i-axes"/></svg></div>
    <div class="tool" style="left:204px"><svg><use href="#i-timer"/></svg></div>
    <div class="tool" style="left:269px"><svg><use href="#i-layers"/></svg></div>
    <div class="tool" style="left:332px"><svg><use href="#i-gear"/></svg></div>
    <div class="tool" style="left:394px"><svg><use href="#i-probe"/></svg></div>
    <div class="tool" style="left:459px"><svg><use href="#i-info"/></svg></div>
    <div class="tool" style="left:518px"><svg><use href="#i-help"/></svg></div>
    <span class="status">Error</span>
    <div class="connect"><svg><use href="#i-connect"/></svg></div>
    <div class="coord cx">X:2.8896</div><div class="coord cy">Y:0.2436</div><div class="coord cz">Z:8.3591</div>
    <span class="check" style="left:20px"></span><span class="label" style="left:44px">Auto Scan</span>
    <span class="check" style="left:192px"></span><span class="label" style="left:218px">Scan Planes</span>
    <span class="label" style="left:372px">Format</span><span class="field" style="left:427px">Tablix</span>
    <span class="label" style="left:735px">Probe</span><span class="field" style="left:785px">Default</span>
  </section>

  <section class="window w2">
    <header class="titlebar"><span class="app-mark"></span><span class="app-title">Haldentrax Utility Software - 7.3</span></header>
    <span class="sep" style="left:15px"></span><span class="sep" style="left:71px"></span><span class="sep" style="left:134px"></span><span class="sep" style="left:197px"></span><span class="sep" style="left:260px"></span><span class="sep" style="left:322px"></span><span class="sep" style="left:385px"></span><span class="sep" style="left:448px"></span><span class="sep" style="left:512px"></span><span class="sep" style="left:573px"></span>
    <div class="tool" style="left:20px"><svg><use href="#i-xyz"/></svg></div>
    <div class="tool" style="left:80px"><svg><use href="#i-grid"/></svg></div>
    <div class="tool" style="left:142px"><svg><use href="#i-axes"/></svg></div>
    <div class="tool" style="left:204px"><svg><use href="#i-timer"/></svg></div>
    <div class="tool active" style="left:269px"><svg><use href="#i-layers"/></svg></div>
    <div class="tool" style="left:332px"><svg><use href="#i-gear"/></svg></div>
    <div class="tool" style="left:394px"><svg><use href="#i-probe"/></svg></div>
    <div class="tool" style="left:459px"><svg><use href="#i-info"/></svg></div>
    <div class="tool" style="left:518px"><svg><use href="#i-help"/></svg></div>
    <span class="status">Error</span>
    <div class="connect"><svg><use href="#i-connect"/></svg></div>
    <div class="coord cx">X:2.8896</div><div class="coord cy">Y:0.2436</div><div class="coord cz">Z:8.3591</div>
    <span class="check" style="left:20px"></span><span class="label" style="left:44px">Auto Scan</span>
    <span class="check" style="left:192px"></span><span class="label" style="left:218px">Scan Planes</span>
    <span class="label" style="left:372px">Format</span><span class="field" style="left:427px">Tablix</span>
    <span class="label" style="left:735px">Probe</span><span class="field" style="left:785px">Default</span>
  </section>

  <section class="window w3">
    <header class="titlebar"><span class="app-mark"></span><span class="app-title">Haldentrax Utility Software - 7.3</span></header>
    <span class="sep" style="left:15px"></span><span class="sep" style="left:71px"></span><span class="sep" style="left:134px"></span><span class="sep" style="left:197px"></span><span class="sep" style="left:260px"></span><span class="sep" style="left:322px"></span><span class="sep" style="left:385px"></span><span class="sep" style="left:448px"></span><span class="sep" style="left:512px"></span><span class="sep" style="left:573px"></span>
    <div class="tool" style="left:20px"><svg><use href="#i-xyz"/></svg></div>
    <div class="tool" style="left:80px"><svg><use href="#i-grid"/></svg></div>
    <div class="tool" style="left:142px"><svg><use href="#i-axes"/></svg></div>
    <div class="tool" style="left:204px"><svg><use href="#i-timer"/></svg></div>
    <div class="tool" style="left:269px"><svg><use href="#i-layers"/></svg></div>
    <div class="tool" style="left:332px"><svg><use href="#i-gear"/></svg></div>
    <div class="tool active" style="left:394px"><svg><use href="#i-probe"/></svg></div>
    <div class="tool" style="left:459px"><svg><use href="#i-info"/></svg></div>
    <div class="tool" style="left:518px"><svg><use href="#i-help"/></svg></div>
    <span class="status">Error</span>
    <div class="connect"><svg><use href="#i-connect"/></svg></div>
    <div class="coord cx">X:2.8896</div><div class="coord cy">Y:0.2436</div><div class="coord cz">Z:8.3591</div>
    <span class="check" style="left:20px"></span><span class="label" style="left:44px">Auto Scan</span>
    <span class="check" style="left:192px"></span><span class="label" style="left:218px">Scan Planes</span>
    <span class="label" style="left:372px">Format</span><span class="field" style="left:427px">Tablix</span>
    <span class="label" style="left:735px">Probe</span><span class="field" style="left:785px">Default</span>
  </section>
</main>
</body>
</html>
```